Craft beer label required for new modern craft brewery

I require a label to be designed for my craft beer, the name of the beer is "Tidewalker Pale Ale".
It has to be a contemporary style label targeting an audience group between the ages of 21-40. It must be unique and appealing.
The label must incorporate the image of a Gladiator which has to originally created (I’m giving you creative freedom), not copied (for copy right reasons). I’m attaching a few examples, please refer to “gladiator1.jpg” and “Gladiator2.jpg”.
It would be nice if the Vandrello could appear in the background, also originally created I’m attaching an example, please refer to “Vandrello1.jpg”
The Label must also incorporate the attached logo “Fennmoor Brewing Co. Craft Beer-01.jpg” .
The label must fit a 440ml bottle
Please use creative freedom with regards to the shape of the label.
The colours do not have to be exactly the same as logo, but obviously they must match.
Updates

Target Market(s)

Modern/contemporary successful 21-40 year olds

Industry/Entity Type

Brewery

Font styles to use
Serif
Script

Colors

Designer to choose colors to be used in the design.

Requirements
Must have
• My logo, the beer name and the image of a gladiator
• The label size should be at least 10cm wide x 9cm wide.
• The label must include the size of the bottle: 440ml
• The label must include 6.5% ALC./VOL.
Nice to have
• Vandrello in the back ground
Should not have
• Copied images or trade marks

```html
<!DOCTYPE html>
<html lang="en">
<head>
<meta charset="utf-8">
<title>Tidewalker Pale Ale – Label</title>
<link rel="stylesheet" href="https://fonts.googleapis.com/css2?family=Playfair+Display+SC:wght@700;900&family=Oswald:wght@500&family=Libre+Baskerville:wght@700&display=swap">
<style>
  :root {
    --backdrop: #ededed;
    --cream: #f6dcbc;
    --cream-light: #fbebd6;
    --peach: #f2c79c;
    --brown: #7a3b1e;
    --brown-dark: #4a2312;
    --gold: #e9ad3f;
    --gold-dark: #b9782a;
    --red: #c0242c;
    --art-warm: #d98a3f;
    --art-deep: #a4521f;
  }
  html, body {
    margin: 0;
    padding: 0;
    width: 1200px;
    height: 1200px;
    overflow: hidden;
    background: var(--backdrop);
  }
  .label-sheet { display: block; width: 1200px; height: 1200px; }
  .label-edge { fill: var(--brown); }
  .label-field { fill: url(#sunburst); }
  .label-rule { fill: none; stroke: var(--brown); stroke-width: 3; }
  .arch-title {
    font-family: "Playfair Display SC", serif;
    font-weight: 700;
    font-size: 54px;
    letter-spacing: 8px;
    fill: var(--red);
  }
  .ribbon-face { fill: var(--gold); stroke: var(--brown); stroke-width: 5; }
  .ribbon-fold { fill: var(--gold-dark); stroke: var(--brown); stroke-width: 4; }
  .beer-name {
    font-family: "Playfair Display SC", serif;
    font-weight: 900;
    font-size: 104px;
    fill: var(--red);
    stroke: var(--brown-dark);
    stroke-width: 2;
  }
  .style-name {
    font-family: "Oswald", sans-serif;
    font-weight: 500;
    font-size: 44px;
    letter-spacing: 4px;
    fill: var(--red);
  }
  .spec {
    font-family: "Libre Baskerville", serif;
    font-weight: 700;
  }
  .spec-abv { font-size: 36px; fill: var(--red); }
  .spec-volume { font-size: 34px; fill: var(--brown-dark); }
  .divider { stroke: var(--brown); stroke-width: 3; }
  .neck-edge { fill: var(--brown); }
  .neck-face { fill: url(#neckGlow); }
  .neck-flap { fill: var(--peach); stroke: var(--brown); stroke-width: 3; }
  .brand-mark { fill: var(--brown-dark); }
  .brand-name {
    font-family: "Playfair Display SC", serif;
    font-weight: 700;
    fill: var(--brown-dark);
  }
  .brand-name-main { font-size: 22px; letter-spacing: 1px; }
  .brand-name-sub { font-size: 22px; letter-spacing: 1px; }
</style>
</head>
<body>
<svg class="label-sheet" viewBox="0 0 1200 1200" xmlns="http://www.w3.org/2000/svg">
  <defs>
    <radialGradient id="sunburst" cx="50%" cy="35%" r="70%">
      <stop offset="0" stop-color="var(--cream-light)"/>
      <stop offset="1" stop-color="var(--cream)"/>
    </radialGradient>
    <radialGradient id="neckGlow" cx="50%" cy="50%" r="60%">
      <stop offset="0" stop-color="var(--cream-light)"/>
      <stop offset="1" stop-color="var(--peach)"/>
    </radialGradient>
    <linearGradient id="heroArt" x1="0" y1="0" x2="1" y2="1">
      <stop offset="0" stop-color="var(--peach)"/>
      <stop offset="0.55" stop-color="var(--art-warm)"/>
      <stop offset="1" stop-color="var(--art-deep)"/>
    </linearGradient>
    <path id="archLine" d="M500,440 A200,230 0 0 1 900,440"/>
  </defs>

  <g class="neck-label">
    <rect class="neck-flap" x="130" y="500" width="220" height="200"/>
    <path class="neck-edge" d="M240,420 C320,420 345,480 345,600 C345,720 320,780 240,780 C160,780 135,720 135,600 C135,480 160,420 240,420 Z"/>
    <path class="neck-face" d="M240,432 C310,432 333,488 333,600 C333,712 310,768 240,768 C170,768 147,712 147,600 C147,488 170,432 240,432 Z"/>
    <circle class="brand-mark" cx="240" cy="545" r="26"/>
    <text class="brand-name brand-name-main" x="240" y="612" text-anchor="middle">FENNMOOR</text>
    <text class="brand-name brand-name-sub" x="240" y="642" text-anchor="middle">BREWING CO.</text>
  </g>

  <g class="main-label">
    <path class="label-edge" d="M430,410 A270,300 0 0 1 970,410 L970,930 Q700,1100 430,930 Z"/>
    <path class="label-field" d="M442,410 A258,288 0 0 1 958,410 L958,924 Q700,1084 442,924 Z"/>
    <path class="label-rule" d="M456,410 A244,274 0 0 1 944,410 L944,916 Q700,1066 456,916 Z"/>

    <text class="arch-title"><textPath href="#archLine" startOffset="50%" text-anchor="middle">CRAFTED BEER</textPath></text>

    <path role="img" aria-label="Illustration of a helmeted gladiator with sword and round shield before an arena in Vandrello" fill="url(#heroArt)" d="M470,560 L470,470 Q480,320 600,290 Q700,270 800,290 Q920,320 930,470 L930,560 Z"/>

    <path class="ribbon-fold" d="M388,730 L442,800 L442,730 Z"/>
    <path class="ribbon-fold" d="M1012,730 L958,800 L958,730 Z"/>
    <rect class="ribbon-face" x="388" y="560" width="624" height="170"/>
    <text class="beer-name" x="700" y="690" text-anchor="middle" textLength="540" lengthAdjust="spacingAndGlyphs">TIDEWALKER</text>

    <line class="divider" x1="520" y1="815" x2="590" y2="815"/>
    <line class="divider" x1="810" y1="815" x2="880" y2="815"/>
    <text class="style-name" x="700" y="831" text-anchor="middle">PALE ALE</text>
    <text class="spec spec-abv" x="700" y="886" text-anchor="middle">6.5% ALC./VOL.</text>
    <text class="spec spec-volume" x="700" y="942" text-anchor="middle">440ml</text>
  </g>
</svg>
</body>
</html>
```